Beyond The Ledger Double Sided DL Flyer

We need a double sided flyer that we provide to a Real Estate agent for leeds. It should provide our basic services as well as a modern look and feel. The brochure should incorporate our Brand colors and have a graphic that centres around money and property. I have included a couple of pictures that we like (but have not yet purchased from PIXVAULT) as an indication of the type of picture we like.

WE need to also show the Beyond The Ledger brand and have our Phone / address's and email details.

Target Market(s)

Realestate clients (Property Investors)

Industry/Entity Type

Financial Planning

Requirements
Must have
• Picture on Front (maybe the logo on back)
• Please incorporate existing logo colours.

```html
<!DOCTYPE html>
<html lang="en">
<head>
<meta charset="utf-8">
<title>Beyond The Ledger – DL Flyer</title>
<link href="https://fonts.googleapis.com/css2?family=Signika:wght@300;400;600;700&display=swap" rel="stylesheet">
<style>
:root{
  --bg:#aeb2ab;
  --green:#79d923;
  --green-bright:#8cf03a;
  --green-deep:#5cbd14;
  --green-text:#6cbf1c;
  --ink:#1c1c1c;
  --white:#ffffff;
}
*{margin:0;padding:0;box-sizing:border-box}
html,body{width:1200px;height:1199px;overflow:hidden;background:var(--bg);font-family:"Signika",sans-serif;color:var(--ink)}
.flyer{position:absolute;top:77px;width:478px;height:1014px;background:var(--white);overflow:hidden;box-shadow:0 8px 24px rgba(0,0,0,.25)}
.flyer--front{left:156px}
.flyer--back{left:677px}
.flyer__art{position:absolute;inset:0;width:100%;height:100%}
.abs{position:absolute}

/* front */
.brand-name{left:0;width:100%;top:626px;text-align:center;font-weight:700;font-size:42px;line-height:1;letter-spacing:-.5px}
.tagline{left:0;width:100%;top:698px;text-align:center;font-weight:600;font-size:11.5px;letter-spacing:.3px}
.website{left:0;width:100%;top:726px;text-align:center;font-weight:700;font-size:27px;color:var(--green-text)}
.headline{left:98px;top:818px;line-height:1}
.headline__strong{font-weight:700;font-size:55px;letter-spacing:-1px;display:block}
.headline__row{display:flex;align-items:flex-end;gap:18px}
.headline__and{font-weight:600;font-size:37px;margin-bottom:44px}
.headline__stack{display:flex;flex-direction:column}
.headline__light{font-weight:300;font-size:56px;letter-spacing:-.5px;margin-top:2px}

/* back */
.brand-name--back{top:50px;left:0;width:100%;text-align:center;color:var(--white);font-size:40px}
.services-title{left:116px;top:112px;display:flex;align-items:center;gap:22px;font-weight:600;font-size:29px}
.services-title__dots{display:flex;gap:14px}
.services-title__dots span{width:9px;height:9px;border:2px solid var(--white);border-radius:50%}
.services{left:36px;top:176px;list-style:none}
.service{display:flex;align-items:center;height:75px;gap:17px}
.service__icon{width:58px;height:58px;border-radius:50%;background:var(--white);box-shadow:0 2px 4px rgba(0,0,0,.15);display:flex;align-items:center;justify-content:center;flex-shrink:0}
.service__text{font-weight:600;font-size:24.5px;line-height:27px}
.advisor{left:60px;top:600px;display:flex;align-items:center;gap:30px}
.advisor__role{font-weight:600;font-size:26px;text-align:center}
.advisor__name{font-weight:700;font-size:41px;line-height:1.05}
.rule{height:3px;background:var(--green)}
.rule--short{left:163px;top:722px;width:229px}
.rule--long{left:85px;top:905px;width:382px}
.addresses{left:84px;top:756px;font-weight:600;font-size:26px;line-height:25px}
.addresses p+p{margin-top:19px}
.phone{left:88px;top:932px;display:flex;align-items:center;gap:20px;font-weight:600;font-size:38px}
</style>
</head>
<body>

<section class="flyer flyer--front">
  <svg class="flyer__art" viewBox="0 0 478 1014" aria-hidden="true">
    <defs>
      <linearGradient id="bandFront" x1="0" y1="0" x2="1" y2="1">
        <stop offset="0" stop-color="#86ec2e"/>
        <stop offset="1" stop-color="#5fcb14"/>
      </linearGradient>
    </defs>
    <path d="M0 785 Q240 745 478 850 V1014 H0 Z" fill="url(#bandFront)"/>
    <circle cx="-10" cy="905" r="78" fill="none" stroke="var(--white)" stroke-width="3"/>
  </svg>
  <svg class="abs" style="left:0;top:0" width="478" height="600" viewBox="0 0 478 600" role="img" aria-label="Photo of a green seedling growing from a pile of coins, with a rising chart line, a house and a family silhouette">
    <defs>
      <linearGradient id="photoTone" x1="0" y1="0" x2="0" y2="1">
        <stop offset="0" stop-color="#6f8d3f"/>
        <stop offset=".35" stop-color="#c9cfb4"/>
        <stop offset=".7" stop-color="#b6a58a"/>
        <stop offset="1" stop-color="#7d6549"/>
      </linearGradient>
    </defs>
    <path d="M0 0 H478 V500 Q240 605 0 505 Z" fill="url(#photoTone)"/>
    <path d="M0 519 Q240 619 478 511" fill="none" stroke="var(--green)" stroke-width="3"/>
  </svg>

  <div class="abs brand-name">Beyond The Ledger</div>
  <div class="abs tagline">BUILD YOUR BUSINESS &amp; GROW YOUR WEALTH</div>
  <div class="abs website">www.beyondtheledger.example</div>

  <div class="abs headline">
    <span class="headline__strong">Accountants</span>
    <div class="headline__row">
      <span class="headline__and">and</span>
      <div class="headline__stack">
        <span class="headline__light">Financial</span>
        <span class="headline__strong">Advisors</span>
      </div>
    </div>
  </div>
</section>

<section class="flyer flyer--back">
  <svg class="flyer__art" viewBox="0 0 477 1014" aria-hidden="true">
    <defs>
      <linearGradient id="bandBack" x1="0" y1="0" x2="1" y2="1">
        <stop offset="0" stop-color="#8cf03a"/>
        <stop offset="1" stop-color="#62cf16"/>
      </linearGradient>
    </defs>
    <path d="M0 0 H477 V490 Q300 640 0 560 Z" fill="url(#bandBack)"/>
    <circle cx="424" cy="84" r="56" fill="none" stroke="#ffffff" stroke-opacity=".25" stroke-width="8"/>
    <circle cx="424" cy="84" r="40" fill="#ffffff" fill-opacity=".12"/>
    <circle cx="570" cy="518" r="86" fill="none" stroke="var(--green)" stroke-width="3"/>
  </svg>

  <div class="abs brand-name brand-name--back">Beyond The Ledger</div>

  <div class="abs services-title">
    <div class="services-title__dots"><span></span><span></span><span></span></div>
    <span>Our Services</span>
  </div>

  <ul class="abs services">
    <li class="service">
      <span class="service__icon"><svg width="34" height="34" viewBox="0 0 34 34" fill="none" stroke="#1c1c1c" stroke-width="2.6"><path d="M4 15 L17 4 L30 15"/><path d="M8 13 V29 H14"/><circle cx="21" cy="22" r="7"/><path d="M17.5 22 H24.5"/></svg></span>
      <span class="service__text">Negative Gearing<br>&amp; Investment Properties</span>
    </li>
    <li class="service">
      <span class="service__icon"><svg width="34" height="34" viewBox="0 0 34 34" fill="none" stroke="#1c1c1c" stroke-width="2.6"><path d="M4 15 L17 4 L30 15"/><path d="M8 13 V29 H14"/><circle cx="21" cy="22" r="7"/><path d="M17.5 22 H24.5 M21 18.5 V25.5"/></svg></span>
      <span class="service__text">Property &amp; Capital Gains<br>Tax Minimisation</span>
    </li>
    <li class="service">
      <span class="service__icon"><svg width="34" height="34" viewBox="0 0 34 34"><circle cx="17" cy="17" r="13" fill="none" stroke="#1c1c1c" stroke-width="2.6"/><text x="17" y="24" text-anchor="middle" font-family="Signika,sans-serif" font-weight="700" font-size="19" fill="#1c1c1c">$</text></svg></span>
      <span class="service__text">Self-Managed<br>Superannuation Funds (SMSF)</span>
    </li>
    <li class="service">
      <span class="service__icon"><svg width="34" height="34" viewBox="0 0 34 34"><text x="17" y="27" text-anchor="middle" font-family="Signika,sans-serif" font-weight="700" font-size="28" fill="#1c1c1c">%</text></svg></span>
      <span class="service__text">Small Business<br>&amp; Personal Taxation</span>
    </li>
    <li class="service">
      <span class="service__icon"><svg width="34" height="34" viewBox="0 0 34 34"><path d="M17 3 L29 8 V16 C29 23 24 28 17 31 C10 28 5 23 5 16 V8 Z" fill="#1c1c1c"/><path d="M11 17 L15.5 21.5 L23 13" fill="none" stroke="#fff" stroke-width="3"/></svg></span>
      <span class="service__text">Investment Advice<br>&amp; Risk Insurances</span>
    </li>
  </ul>

  <div class="abs advisor">
    <svg width="86" height="86" viewBox="0 0 86 86" aria-hidden="true"><circle cx="43" cy="43" r="42" fill="var(--green)"/><circle cx="43" cy="35" r="17" fill="#fff"/><path d="M14 74 C20 58 66 58 72 74 A42 42 0 0 1 14 74 Z" fill="#fff"/></svg>
    <div>
      <div class="advisor__role">Advisor / Accountant</div>
      <div class="advisor__name">Owen Hartley</div>
    </div>
  </div>
  <div class="abs rule rule--short"></div>

  <div class="abs addresses">
    <p>4 / 118 Harbour View Rd<br>Lakeside NSW 2251</p>
    <p>2 / 71 Marine Pde Bayview<br>NSW 2264 (By Appointment)</p>
  </div>
  <div class="abs rule rule--long"></div>

  <div class="abs phone">
    <svg width="42" height="42" viewBox="0 0 24 24" aria-hidden="true"><path fill="#1c1c1c" d="M6.6 10.8a15.1 15.1 0 0 0 6.6 6.6l2.2-2.2a1 1 0 0 1 1-.25 11.4 11.4 0 0 0 3.6.57 1 1 0 0 1 1 1V20a1 1 0 0 1-1 1A17 17 0 0 1 3 4a1 1 0 0 1 1-1h3.5a1 1 0 0 1 1 1c0 1.25.2 2.45.57 3.570a1 1 0 0 1-.25 1Z"/></svg>
    <span>(02) 4555 0192</span>
  </div>
</section>

</body>
</html>
```